New Packaging Design Project

Wine packaging redesign. Retail partner requested a redesign of a private label wine. The old label is attached. Our partner liked the Lantern and Briar label and wanted something similar. There will be a logo added to the top of the label

Went on vacation/holiday

```html
<!DOCTYPE html>
<html lang="en">
<head>
<meta charset="UTF-8">
<title>Cedar Hollow Red Blend – Label</title>
<link rel="stylesheet" href="https://fonts.googleapis.com/css2?family=Cormorant+Garamond:wght@500;600&family=Oswald:wght@300;400&display=swap">
<style>
  :root {
    --backdrop: #e7e5de;
    --label: #3a3c3f;
    --gold: #dba347;
    --gold-muted: #8a7349;
    --silver: #d9dadb;
    --mist: #9c9fa2;
    --hill: #55585d;
    --navy-shadow: #2c3343;
  }
  * { margin: 0; padding: 0; box-sizing: border-box; }
  html, body {
    width: 1200px;
    height: 780px;
    overflow: hidden;
    background: var(--backdrop);
  }
  .canvas {
    position: relative;
    width: 1200px;
    height: 780px;
    display: flex;
    align-items: center;
    justify-content: center;
  }
  .wine-label {
    position: relative;
    width: 416px;
    height: 700px;
    background: var(--label);
    box-shadow: 0 10px 30px rgba(0, 0, 0, 0.12);
    overflow: hidden;
  }
  .wine-name {
    position: absolute;
    top: 70px;
    left: 0;
    right: 0;
    text-align: center;
    font-family: "Cormorant Garamond", "Times New Roman", serif;
    font-weight: 600;
    font-size: 42px;
    line-height: 54px;
    letter-spacing: 1px;
    color: var(--gold);
    text-transform: uppercase;
  }
  .wine-style {
    position: absolute;
    top: 144px;
    left: 0;
    right: 0;
    text-align: center;
    font-family: "Oswald", "Arial Narrow", sans-serif;
    font-weight: 400;
    font-size: 19px;
    line-height: 28px;
    letter-spacing: 3px;
    color: var(--silver);
    text-transform: uppercase;
  }
  .vintage {
    position: absolute;
    top: 184px;
    left: 0;
    right: 0;
    text-align: center;
    font-family: "Cormorant Garamond", "Times New Roman", serif;
    font-weight: 600;
    font-size: 28px;
    line-height: 36px;
    letter-spacing: 1px;
    font-variant-numeric: lining-nums;
    color: var(--gold);
  }
  .landscape-art {
    position: absolute;
    top: 258px;
    left: 0;
    width: 416px;
    height: 360px;
    background: linear-gradient(180deg,
      var(--label) 0%,
      var(--gold-muted) 14%,
      var(--mist) 34%,
      var(--hill) 58%,
      var(--navy-shadow) 82%,
      var(--label) 100%);
  }
  .grape-list {
    position: absolute;
    top: 624px;
    left: 0;
    right: 0;
    text-align: center;
    font-family: "Oswald", "Arial Narrow", sans-serif;
    font-weight: 300;
    font-size: 14px;
    line-height: 23px;
    letter-spacing: 2px;
    color: var(--silver);
    text-transform: uppercase;
  }
</style>
</head>
<body>
  <main class="canvas">
    <section class="wine-label">
      <h1 class="wine-name">Cedar Hollow</h1>
      <p class="wine-style">Red Blend</p>
      <p class="vintage">2018</p>
      <div class="landscape-art" role="img" aria-label="Illustration of a golden sun rising behind layered grey hills, with dark vineyard rows fanning out in thin gold lines"></div>
      <p class="grape-list">
        Merlot • Cabernet Sauvignon<br>
        Cabernet Franc • Petit Verdot • Malbec
      </p>
    </section>
  </main>
</body>
</html>
```